Bright Path Mentoring Brochure

Looking for a tri-fold brochure that can work as a self-mailer and a leave behind piece.

Bright Path Mentoring works with parents and young teens to develop personal capacity; emotional intelligence, resilience, communications skills, goal setting, and a high level of consciousness and attitude control. See our website at www.brightpathmentoring.example.

Cover should be provocative... quote about 46% of entering freshman from the website is powerful

We are talking about a 11"x8.5" opened, 3.7 x 8.5 folded tri-fold... there should be plenty of content on our website... The inside panels could be as follows

left panel could be a graphic and part of "the Story" Head line about 46% of entering freshman taking more than 6 years to get a degree.

Middle and right panels could be the three programs... Attitudinal Assessment, Group coaching on Communication, Value based S.M.A.R.T. goal setting and defeating internal blocks. and One on One Family coaching.

Target Market(s)

Parents and teens in the 9th grade age range

Industry/Entity Type

Communications

Requirements
Must have
• Provocative Title
"Did you know 46% of entering college freshman fail to receive a degree within 6 years?"
Powerful graphics to communicate transformation from anger and conflict between parents and teens to collaboration and cooperation.

```html
<!DOCTYPE html>
<html lang="en">
<head>
<meta charset="utf-8">
<title>Bright Path Mentoring – Tri-fold Brochure</title>
<link href="https://fonts.googleapis.com/css2?family=Arimo:wght@400;700&family=Open+Sans:wght@300;400;600;700&display=swap" rel="stylesheet">
<style>
  :root{
    --bg:#e9e6e1;
    --paper:#ffffff;
    --panel-grey:#e4e4e4;
    --ink:#1d1d1d;
    --navy:#1f3f6b;
    --navy-dark:#1b355c;
    --crimson:#8e1b2c;
    --maroon:#5a1117;
    --maroon-mid:#7a1624;
    --green:#1f7a2e;
    --green-bright:#178a2a;
    --charcoal:#252323;
    --fold:#c9c9c9;
    --light:#f5f5f5;
  }
  *{box-sizing:border-box;margin:0;padding:0}
  html,body{width:1200px;height:900px;overflow:hidden}
  body{background:var(--bg);font-family:"Open Sans",Arial,sans-serif;color:var(--ink);position:relative}

  .sheet{position:absolute;width:580px;height:448px;background:var(--paper);box-shadow:0 4px 14px rgba(0,0,0,.18);overflow:hidden}
  .sheet--outside{left:13px;top:226px;display:flex}
  .sheet--inside{left:607px;top:226px}

  /* ---------- outside ---------- */
  .panel{position:relative;width:193.3px;height:100%;border-right:1px solid var(--fold)}
  .panel:last-child{border-right:none}
  .panel--mailer{background:linear-gradient(135deg,#f2f2f2,#d9d9d9)}
  .panel--cover-text{background:linear-gradient(180deg,#f0f0f0,#e2e2e2)}
  .panel--front{background:linear-gradient(180deg,#f4f4f4,#e6e6e6)}

  .contact-card{position:absolute;left:26px;bottom:26px;width:140px;height:214px;background:var(--charcoal);color:#e8e8e8;text-align:center;padding-top:44px}
  .brand{display:flex;flex-direction:column;align-items:center;gap:6px}
  .brand__dot{width:26px;height:26px;border-radius:50%;background:var(--green)}
  .brand__name{font-family:"Arimo",Arial,sans-serif;font-weight:400;font-size:13px;line-height:1.15}
  .contact-card .brand__name{color:#f2f2f2}
  .contact-card address{font-style:normal;font-size:8px;line-height:1.55;margin-top:26px}

  .cover-text{position:absolute;inset:0;padding:96px 10px 0 14px;font-family:"Arimo",Arial,sans-serif}
  .cover-text__lead{font-weight:700;font-size:25px;text-align:right;padding-right:4px;letter-spacing:-.3px}
  .stat-box{display:inline-block;color:#fff;font-family:"Open Sans",Arial,sans-serif;font-weight:300;line-height:1}
  .stat-box--percent{background:var(--navy);font-size:46px;padding:8px 12px 10px;margin:22px 0 0 30px}
  .stat-box--fail{background:var(--crimson);font-size:46px;padding:4px 14px 10px;margin:12px 0 0 82px}
  .cover-text__line{font-weight:700;font-size:15px;line-height:1.2}
  .cover-text__line--right{text-align:right;margin-top:10px}
  .cover-text__line--left{margin-top:12px;padding-left:62px}

  .photo{display:block}
  .front-photo{position:absolute;left:14px;width:168px;height:134px}
  .front-photo--top{top:12px;background:linear-gradient(160deg,var(--green-bright),#14601f)}
  .front-photo--bottom{bottom:14px;background:linear-gradient(160deg,#6a1a1e,#3f0d11)}
  .front-brand{position:absolute;top:166px;left:0;right:0;text-align:center}
  .front-brand .brand__name{font-size:19px;color:var(--ink)}
  .front-brand .brand__dot{width:34px;height:34px}
  .tagline{font-size:6px;font-style:italic;color:#444;margin-top:3px}

  /* ---------- inside ---------- */
  .headline-band{position:absolute;left:0;top:0;width:100%;height:70px;background:var(--maroon);color:#fff;font-family:"Arimo",Arial,sans-serif}
  .headline-band .stat-box{position:absolute;background:var(--maroon-mid);border:1px solid #8a2a35;font-size:30px;padding:6px 10px 8px}
  .headline-band .stat-box--in-percent{left:12px;top:20px}
  .headline-band .stat-box--in-fail{left:206px;top:8px}
  .headline-band__of{position:absolute;left:96px;top:30px;font-weight:700;font-size:12px;line-height:1.05}
  .headline-band__rest{position:absolute;left:272px;top:12px;font-weight:700;font-size:10.5px;line-height:1.25;width:300px}
  .headline-band__source{position:absolute;right:12px;top:52px;font-size:8px;font-style:italic;color:#e6cfd1}

  .inside-columns{position:absolute;left:0;top:70px;width:100%;height:378px;display:flex;background:#f1f1f1;padding:10px 6px 8px}
  .column{width:33.33%;margin:0 4px;color:#fff;font-size:5.6px;line-height:1.45;padding:7px 7px;overflow:hidden;position:relative}
  .column--story{background:var(--green)}
  .column--assessment{background:var(--crimson)}
  .column--programs{background:var(--navy)}
  .column h3{font-size:6.4px;font-weight:700;margin:3px 0 3px}
  .column p{margin-bottom:5px}
  .column h4{font-size:6px;font-weight:700;margin:4px 0 3px}
  .inline-photo{float:right;margin:0 0 4px 5px}
  .inline-photo--grads{width:58px;height:36px;background:linear-gradient(135deg,#eaeaea,#3a3a3a)}
  .inline-photo--chart{float:left;margin:0 5px 4px 0;width:52px;height:46px;background:linear-gradient(135deg,#f4f4f4,#b9d99b)}
  .inline-photo--coins{width:50px;height:40px;background:linear-gradient(135deg,#f2f2f2,#a9a9a9)}
  .inline-photo--figures{width:50px;height:34px;background:linear-gradient(135deg,#f5f5f5,#c9c9c9)}
  .inline-photo--reader{width:46px;height:38px;background:linear-gradient(135deg,#eeeeee,#c7b39a)}
</style>
</head>
<body>

<section class="sheet sheet--outside" aria-label="Brochure outside">
  <div class="panel panel--mailer">
    <div class="contact-card">
      <div class="brand">
        <span class="brand__dot"></span>
        <span class="brand__name">Bright Path<br>Mentoring</span>
      </div>
      <address>
        218 Linden Court<br>
        Suite 40-B<br>
        Fairview, VA 20199<br>
        kellyrt4success@example.com<br>
        (555) 014-7012
      </address>
    </div>
  </div>

  <div class="panel panel--cover-text">
    <div class="cover-text">
      <p class="cover-text__lead">Did you know?</p>
      <span class="stat-box stat-box--percent">46%</span>
      <p class="cover-text__line cover-text__line--right">of entering<br>college freshman</p>
      <span class="stat-box stat-box--fail">fail</span>
      <p class="cover-text__line cover-text__line--left">to receive a<br>degree within<br>6 years?</p>
    </div>
  </div>

  <div class="panel panel--front">
    <div class="photo front-photo front-photo--top" role="img" aria-label="Photo of parents and teen working together"></div>
    <div class="front-brand">
      <div class="brand">
        <span class="brand__dot"></span>
        <span class="brand__name">Bright Path Mentoring</span>
      </div>
      <p class="tagline">"We Coach Parents and Their Teens To Optimal Success"</p>
    </div>
    <div class="photo front-photo front-photo--bottom" role="img" aria-label="Photo of a family in conversation"></div>
  </div>
</section>

<section class="sheet sheet--inside" aria-label="Brochure inside">
  <header class="headline-band">
    <span class="stat-box stat-box--in-percent">46%</span>
    <p class="headline-band__of">of college<br>freshmen</p>
    <span class="stat-box stat-box--in-fail">fail</span>
    <p class="headline-band__rest">to get a degree within 6 years; for those who do, graduation is no guarantee of success.</p>
    <p class="headline-band__source">Northfield Education Trust</p>
  </header>

  <div class="inside-columns">
    <article class="column column--story">
      <div class="photo inline-photo inline-photo--grads" role="img" aria-label="Photo of graduates in caps and gowns"></div>
      <p>In this age of right-sized staffs, tight budgets and squeezed profits employers are increasingly concerned about hiring recent grads whose personal capacity lags far behind their personal capability. It's not the recent grads' fault. They are behaving exactly as they were prepared to behave.</p>
      <div class="photo inline-photo inline-photo--chart" role="img" aria-label="Illustration of a coach beside a growth diagram"></div>
      <p>The fact is, educational institutions, secondary and post-secondary, spend little if any time developing personal capacity in their students. They simply are not set up to do so. In the past, personal capacity was developed in the home and community. However, changing dynamics – single parent homes, two income homes and over-scheduled lives – have diminished the amount of emotional development being received by kids, especially those in the all-important 14-17 age range.</p>
      <p>This may explain why college dropout rates were called a "national crisis" in a 2013 research report funded by the Northfield Education Trust. The report found that 46% of entering college freshman do not earn a degree within 6 years, all at a time when college tuitions are rising faster than household incomes.</p>
      <div class="photo inline-photo inline-photo--coins" role="img" aria-label="Photo of coins and a pocket watch"></div>
      <p>Today, parents are fixated on getting their child into a good college or university with little thought about how to set them up for success once they get there. They believe a good GPA and test scores are the holy grail. Imagine their surprise when their academic superstar washes out after only 2 years and $24K–$60K of their hard earned money has gone down the drain.</p>
    </article>

    <article class="column column--assessment">
      <h3>Bright Path Assessment</h3>
      <p>The Bright Path Mentoring process begins with a comprehensive attitudinal assessment of each team member individually, and the team as a whole. Using the highly respected Core Energy Profile (CEP) assessment tool we determine each person's default attitudinal response under normal conditions and under stress. We produce a similar determination for the team as a whole.</p>
      <p>The assessment tool is administered online and requires approximately 20 minutes to complete. Results are available to the coach practitioner immediately. The assessment includes a comprehensive debrief for each individual and for the team conducted by a master practitioner trained and certified to administer and debrief the assessment.</p>
      <p>The individual debrief is conducted either in person or via live video online. The team debrief is conducted in person with all team members. Both debriefs take approximately one hour to complete. Individual results will not be shared by the coach with other team members. We do encourage team members to share their results openly.</p>
      <h3>What does the assessment tell us?</h3>
      <p>The Core Energy Profile assessment provides insights into how you show up in various aspects of your life. It measures your potential leadership ability by your level of consciousness – your awareness about who you are and what life is about.</p>
      <div class="photo inline-photo inline-photo--figures" role="img" aria-label="Illustration of two figures talking"></div>
      <p>Including yourself, to take positive, productive and sustainable action. The assessment also measures how involved or engaged you are in your roles and tasks on the job, at school and at home.</p>
      <p>Finally, the assessment shows your energetic reaction to stress so that you can recognize and, if desired, modify that reaction.</p>
    </article>

    <article class="column column--programs">
      <h3>Bright Path Group Coaching — Teens and Adults<br>(3) 2-1/2 hour sessions held once a week for 3 weeks</h3>
      <p>We encounter communications roadblocks everyday where we live, work, and play. Early cultural learning and learned patterns of attitudinal response affect how we think, feel and act toward other people and enhance or undermine our ability to communicate effectively. We discover specific styles of communication, including different types of conflict communication – the unproductive, aggressive approach that almost always fosters a conversation's fast downward spiral.</p>
      <p>In our Effective Communications Workshop you will learn how to facilitate bridge-building, even when you resolve differences with others. Just as important, you'll learn the basics of perhaps the most important and neglected aspect of human communication, the art of actually listening, the only form of communicating that helps solve problems and simultaneously enhance relationships at home, school or in the workplace.</p>
      <h4>Goal Setting Workshop</h4>
      <div class="photo inline-photo inline-photo--reader" role="img" aria-label="Photo of a teen reading"></div>
      <p>Setting goals is a fundamental component to long-term success. The basic reason for this is that we can't get where we are trying to go until we clearly define where that is. Research studies show a direct link between goals and enhanced performance in life. Goals help us focus and allocate our time and resources efficiently, and they keep us motivated when we feel like giving up.</p>
      <p>Goals help us stay aware of what is expected from us and leave little room for us to hide behind the curtain of unspoken expectations. Furthermore, setting and achieving goals translates to feelings of success for both individuals and groups, which in turn spurs greater productivity and confidence.</p>
    </article>
  </div>
</section>

</body>
</html>
```